Criação de Capa para Facebook para Viagens & Lazer
A empresa queria:
" Adquirindo, ofertando e vendendo pontos e milhas dos programas de fidelidade. "

```html
<!DOCTYPE html>
<html lang="pt">
<head>
<meta charset="utf-8">
<title>Capa para Facebook – Milha Certa</title>
<link rel="stylesheet" href="https://fonts.googleapis.com/css2?family=Montserrat:wght@600&display=swap">
<style>
  :root {
    --page-bg: #eceef2;
    --navy: #14254a;
    --navy-deep: #0b1733;
    --brand-blue: #2a6fcf;
    --paper: #ffffff;
    --ink: #1c2230;
    --sky-top: #1d2f52;
    --sky-mid: #3b4f78;
    --glow: #d99a86;
    --plane: #dfe3ea;
  }
  html, body {
    margin: 0;
    width: 1200px;
    height: 1200px;
    overflow: hidden;
    background: var(--page-bg);
  }
  .cover {
    position: absolute;
    left: 0;
    top: 371px;
    width: 1200px;
    height: 457px;
    overflow: hidden;
    background: var(--paper);
  }
  .cover-art {
    position: absolute;
    inset: 0;
    width: 1200px;
    height: 457px;
  }
  .brand {
    position: absolute;
    left: 780px;
    top: 250px;
    width: 380px;
    display: flex;
    align-items: center;
    justify-content: center;
    gap: 14px;
  }
  .brand-mark {
    flex: none;
    width: 18px;
    height: 18px;
    background: var(--brand-blue);
  }
  .brand-name {
    margin: 0;
    font-family: "Montserrat", Arial, sans-serif;
    font-weight: 600;
    font-size: 38px;
    line-height: 1;
    color: var(--ink);
    white-space: nowrap;
  }
</style>
</head>
<body>
  <section class="cover" aria-label="Capa de página para Facebook">
    <svg class="cover-art" viewBox="0 0 1200 457" xmlns="http://www.w3.org/2000/svg">
      <defs>
        <linearGradient id="dusk-photo" x1="0" y1="0" x2="0.4" y2="1">
          <stop offset="0" stop-color="#1d2f52"/>
          <stop offset="0.45" stop-color="#3b4f78"/>
          <stop offset="0.7" stop-color="#dfe3ea"/>
          <stop offset="1" stop-color="#d99a86"/>
        </linearGradient>
      </defs>
      <polygon class="photo-area" role="img"
               aria-label="Fotografia de um avião comercial estacionado no aeroporto ao entardecer"
               points="0,0 760,0 640,457 0,457" fill="url(#dusk-photo)"/>
      <polygon class="edge-band" points="760,0 782,0 662,457 640,457" fill="var(--navy)"/>
      <polygon class="corner-accent" points="980,0 1200,0 1200,250" fill="var(--navy-deep)"/>
    </svg>
    <div class="brand">
      <span class="brand-mark"></span>
      <p class="brand-name">Milha Certa</p>
    </div>
  </section>
</body>
</html>
```